R. T. HOLLOWAY, INC. is a US based Investment firm looking for a five-page website design.

Currently, their temporary site is located at: rtholloway.com and they would like to maintain the site design as much as possible.

R. T. HOLLOWAY, INC. sister companies are: Crestvale Lodge Investments (c-lodge.com) Benwick Petroleum (benwick-petroleum.com) and RTHF (rth-foundation.org/en)

Attached is a .ZIP file with designs and assets we think will be useful for your proposal… Content for the site is attached on: rtholloway website content.docx Current temp website design is attached as: Coming Soon Website.zip .EPS Logo files attached as: rtholloway logos.zip Sample business card attached as: R T Holloway Business cards.eps Other assets, such as Fonts and background images attached as: Assets.zip

Target Market(s)

Investors

Industry/Entity Type

Investments

Number of Pages Required

5+ page

Requirements
Must have
• Contact Page with a form.

```html
<!DOCTYPE html>
<html lang="en">
<head>
<meta charset="utf-8">
<title>R. T. Holloway, Inc.</title>
<link href="https://fonts.googleapis.com/css2?family=Cinzel:wght@400;500;600&family=Open+Sans:wght@400;600&display=swap" rel="stylesheet">
<style>
:root{
  --navy:#22252e;
  --navy-card:#1f2433;
  --gold:#9b8455;
  --gold-light:#b39a66;
  --ink:#2a2d36;
  --text:#3a3d45;
  --white:#ffffff;
  --ring:#efebe4;
}
*{margin:0;padding:0;box-sizing:border-box}
html,body{width:1200px;height:3299px;overflow:hidden;background:var(--white)}
body{font-family:"Open Sans",sans-serif;color:var(--text);position:relative}
.serif{font-family:"Cinzel",serif}
a{color:inherit;text-decoration:none}

/* header */
.site-header{position:absolute;top:0;left:0;width:1200px;height:143px;display:flex;align-items:center;padding:0 111px;justify-content:space-between}
.brand{display:flex;flex-direction:column;align-items:center;width:200px}
.brand-dot{width:50px;height:50px;border:3px solid var(--ink);border-radius:50%;margin-bottom:8px}
.brand-name{font-family:"Cinzel",serif;font-size:26px;color:var(--ink);letter-spacing:.5px;white-space:nowrap}
.brand-sub{font-family:"Cinzel",serif;font-size:14px;color:var(--ink)}
.main-nav{display:flex;gap:29px;font-family:"Cinzel",serif;font-size:14px;color:var(--ink);letter-spacing:.5px}
.main-nav .active{color:var(--gold)}

/* hero */
.hero{position:absolute;top:143px;left:0;width:1200px;height:547px;overflow:hidden}
.hero-photo{position:absolute;inset:0;background:linear-gradient(180deg,#e0a873 0%,#d9a07e 22%,#a38a88 45%,#6c7079 60%,#8a8d93 72%,#a4a6aa 100%)}
.hero-ring{position:absolute;left:793px;top:210px;width:440px;height:440px;border:14px solid rgba(255,255,255,.28);border-radius:50%}
.hero-copy{position:absolute;left:111px;top:186px;color:var(--white);width:420px}
.hero-kicker{font-family:"Cinzel",serif;font-size:14px;letter-spacing:.5px}
.hero-title{font-family:"Cinzel",serif;font-size:28px;font-weight:400;letter-spacing:1px;margin:4px 0 14px}
.hero-text{font-size:13px;line-height:26px}
.btn-outline-light{display:inline-block;margin-top:14px;border:1px solid var(--white);padding:8px 27px;font-size:13px;color:var(--white)}

/* section heading */
.section-head{display:flex;flex-direction:column;align-items:center}
.mark{width:68px;height:68px;border:3px solid var(--ink);border-radius:50%}
.section-title{font-family:"Cinzel",serif;font-weight:500;font-size:32px;color:var(--ink);margin-top:8px;letter-spacing:1px}
.rule{width:58px;height:1px;background:var(--ink);margin-top:8px}

.deco-ring{position:absolute;border:18px solid var(--ring);border-radius:50%}

/* about */
.about{position:absolute;top:690px;left:0;width:1200px;height:438px;overflow:hidden;text-align:center}
.about .section-head{margin-top:55px}
.body-copy{font-size:13px;line-height:19px;color:var(--text);width:830px;margin:20px auto 0}
.btn-outline{display:inline-block;border:1px solid var(--ink);padding:8px 24px;font-size:14px;color:var(--ink);margin-top:22px;background:var(--white)}

/* mission / vision */
.pillars{position:absolute;top:1128px;left:0;width:1200px;height:379px;display:flex}
.pillar{width:600px;height:379px;position:relative;overflow:hidden;text-align:center;color:var(--white)}
.pillar.mission{background:var(--navy)}
.pillar.vision{background:var(--gold)}
.pillar .mark{border-color:var(--white);margin:70px auto 0}
.pillar h2{font-family:"Cinzel",serif;font-weight:500;font-size:32px;margin-top:10px;letter-spacing:1px}
.pillar .rule{background:var(--white);margin:6px auto 0}
.pillar p{font-size:13px;line-height:19px;width:390px;margin:22px auto 0;position:relative}
.vision-ring{position:absolute;left:235px;top:43px;width:430px;height:430px;border:22px solid rgba(80,70,50,.35);border-radius:50%}

/* investments */
.investments{position:absolute;top:1507px;left:0;width:1200px;height:950px}
.investments .section-head{margin-top:62px}
.cards{position:absolute;top:211px;left:111px;width:978px;display:grid;grid-template-columns:repeat(3,312px);column-gap:21px;row-gap:22px}
.card{height:345px;background:var(--navy-card);border-radius:0 0 8px 8px;overflow:hidden;color:var(--white)}
.card.featured{background:var(--gold);box-shadow:0 4px 14px rgba(0,0,0,.2)}
.card-photo{height:224px}
.card-body{padding:14px 16px 0}
.card-title{font-family:"Cinzel",serif;font-size:18px;font-weight:500;letter-spacing:1px}
.card-text{font-size:13px;line-height:21px;margin-top:4px}
.card-link{display:flex;justify-content:flex-end;align-items:center;gap:4px;font-family:"Cinzel",serif;font-size:14px;margin-top:5px;padding-right:6px}
.p-energy{background:linear-gradient(160deg,#4a63a8,#8fa6d8 40%,#2d3b5e 75%,#1c2540)}
.p-mining{background:linear-gradient(160deg,#5a5a58,#3a3a38 50%,#c89a2e 70%,#2b2b2a)}
.p-industry{background:linear-gradient(160deg,#1a2a4a,#2e4270 45%,#c0562e 75%,#20283c)}
.p-finance{background:linear-gradient(160deg,#6f8fc2,#2f4f88 50%,#1d2f55)}
.p-health{background:linear-gradient(160deg,#a9c7e4,#dbe7f3 45%,#7aa2cb 75%,#c8d9ea)}
.p-estate{background:linear-gradient(160deg,#6e7f96,#c68a52 45%,#e2e4e8 75%,#3d4a5e)}

/* social */
.social{position:absolute;top:2457px;left:0;width:1200px;height:403px;overflow:hidden;text-align:center}
.social .section-head{margin-top:85px}

/* footer */
.footer-tab{position:absolute;top:2860px;left:413px;width:374px;height:80px;background:var(--navy)}
.site-footer{position:absolute;top:2930px;left:0;width:1200px;height:369px;background:var(--navy);color:var(--white);text-align:center}
.footer-mark{position:absolute;top:-70px;left:558px;width:84px;height:84px;border:3px solid var(--gold);border-radius:50%}
.footer-name{font-family:"Cinzel",serif;font-size:42px;margin-top:43px;letter-spacing:1px}
.footer-sub{font-family:"Cinzel",serif;font-size:22px;color:var(--gold);margin-top:-4px}
.contact-line{display:flex;justify-content:center;align-items:center;gap:14px;font-family:"Cinzel",serif;font-size:16px;margin-top:42px}
.contact-line svg{width:14px;height:14px;fill:var(--white);margin-right:6px;vertical-align:-1px}
.footer-nav{display:flex;justify-content:center;gap:31px;font-family:"Cinzel",serif;font-size:14px;margin-top:30px}
.social-links{display:flex;justify-content:center;gap:20px;margin-top:20px}
.social-links span{width:24px;height:24px;border-radius:50%;background:var(--white)}
.copyright{font-family:"Cinzel",serif;font-size:13px;margin-top:30px;letter-spacing:.5px}
</style>
</head>
<body>

<header class="site-header">
  <div class="brand">
    <span class="brand-dot"></span>
    <span class="brand-name">R. T. Holloway</span>
    <span class="brand-sub">Inc.</span>
  </div>
  <nav class="main-nav">
    <a class="active">Home</a><a>About Us</a><a>Investment Areas</a><a>Social Responsibility</a><a>Contact Us</a>
  </nav>
</header>

<section class="hero">
  <div class="hero-photo" role="img" aria-label="City skyline at sunset seen across an empty paved plaza"></div>
  <div class="hero-ring"></div>
  <div class="hero-copy">
    <div class="hero-kicker">Welcome to</div>
    <h1 class="hero-title">R. T. Holloway, Inc.</h1>
    <p class="hero-text">R. T. Holloway, Inc. helps develop into a great nation and, with assertiveness, stamp its footprint worldwide.</p>
    <a class="btn-outline-light">Get Started Now</a>
  </div>
</section>

<section class="about">
  <div class="deco-ring" style="left:-170px;top:95px;width:580px;height:580px"></div>
  <div class="section-head" style="position:relative">
    <span class="mark"></span>
    <h2 class="section-title">About Us</h2>
    <span class="rule"></span>
  </div>
  <p class="body-copy" style="position:relative">Based in Houston, Texas, R. T. Holloway, Inc. is an investment company, founded in 2010, with the purpose to foster endeavors for socioeconomic development, and create platforms for harnessing the potential of world resources, designed to meet the demands of the emerging markets. R. T. Holloway, Inc. functions as a vehicle that enables investments, with the goal of developing the multiple opportunities available.</p>
  <p class="body-copy" style="position:relative;margin-top:19px">R. T. Holloway, Inc. holds interests in areas of investment that are vital to the international economy: Sectors of Energy, Mining, Industry, Finance and Real Estate.</p>
  <a class="btn-outline" style="position:relative">Read More About Us</a>
</section>

<section class="pillars">
  <div class="pillar mission">
    <span class="mark"></span>
    <h2>Mission</h2>
    <span class="rule" style="display:block"></span>
    <p>Build a legacy for future generations through a differentiated selection and the development of, safe and high return investment opportunities for our customers, partners, and shareholders, generating a positive impact on the communities it serves.</p>
  </div>
  <div class="pillar vision">
    <div class="vision-ring"></div>
    <span class="mark" style="position:relative;display:block"></span>
    <h2 style="position:relative">Vision</h2>
    <span class="rule" style="display:block;position:relative"></span>
    <p>R. T. Holloway, Inc. is the main private investment company working towards the diversification and consolidation of national and regional economy.</p>
  </div>
</section>

<section class="investments">
  <div class="section-head">
    <span class="mark"></span>
    <h2 class="section-title">Investment Areas</h2>
    <span class="rule"></span>
  </div>
  <div class="cards">
    <article class="card"><div class="card-photo p-energy" role="img" aria-label="Power plant cooling towers and pylons by a lake at dusk"></div><div class="card-body"><h3 class="card-title">Energy</h3><p class="card-text">R. T. Holloway, Inc. holds investments both in Exploration &amp; Production, and supportfield</p><a class="card-link">Read More <svg width="12" height="12" viewBox="0 0 12 12"><path d="M1 6h8M6 2l4 4-4 4" stroke="#fff" stroke-width="2" fill="none"/></svg></a></div></article>
    <article class="card featured"><div class="card-photo p-mining" role="img" aria-label="Wheel loader filling a dump truck at a mine"></div><div class="card-body"><h3 class="card-title">Mining</h3><p class="card-text">R. T. Holloway, Inc. holds investments both in Exploration &amp; Production, and supportfield</p><a class="card-link">Read More <svg width="12" height="12" viewBox="0 0 12 12"><path d="M1 6h8M6 2l4 4-4 4" stroke="#fff" stroke-width="2" fill="none"/></svg></a></div></article>
    <article class="card"><div class="card-photo p-industry" role="img" aria-label="Industrial refinery lit at night"></div><div class="card-body"><h3 class="card-title">Industry</h3><p class="card-text">R. T. Holloway, Inc. holds investments both in Exploration &amp; Production, and supportfield</p><a class="card-link">Read More <svg width="12" height="12" viewBox="0 0 12 12"><path d="M1 6h8M6 2l4 4-4 4" stroke="#fff" stroke-width="2" fill="none"/></svg></a></div></article>
    <article class="card"><div class="card-photo p-finance" role="img" aria-label="Stacks of coins with a rising financial chart"></div><div class="card-body"><h3 class="card-title">Finance</h3><p class="card-text">R. T. Holloway, Inc. holds investments both in Exploration &amp; Production, and supportfield</p><a class="card-link">Read More <svg width="12" height="12" viewBox="0 0 12 12"><path d="M1 6h8M6 2l4 4-4 4" stroke="#fff" stroke-width="2" fill="none"/></svg></a></div></article>
    <article class="card"><div class="card-photo p-health" role="img" aria-label="Medical researcher working with a digital interface"></div><div class="card-body"><h3 class="card-title">Healthcare</h3><p class="card-text">R. T. Holloway, Inc. holds investments both in Exploration &amp; Production, and supportfield</p><a class="card-link">Read More <svg width="12" height="12" viewBox="0 0 12 12"><path d="M1 6h8M6 2l4 4-4 4" stroke="#fff" stroke-width="2" fill="none"/></svg></a></div></article>
    <article class="card"><div class="card-photo p-estate" role="img" aria-label="Model house beside a hand signing a contract"></div><div class="card-body"><h3 class="card-title">Real Estate</h3><p class="card-text">R. T. Holloway, Inc. holds investments both in Exploration &amp; Production, and supportfield</p><a class="card-link">Read More <svg width="12" height="12" viewBox="0 0 12 12"><path d="M1 6h8M6 2l4 4-4 4" stroke="#fff" stroke-width="2" fill="none"/></svg></a></div></article>
  </div>
</section>

<section class="social">
  <div class="deco-ring" style="left:-170px;top:120px;width:580px;height:580px"></div>
  <div class="section-head" style="position:relative">
    <span class="mark"></span>
    <h2 class="section-title">Social Responsibility</h2>
    <span class="rule"></span>
  </div>
  <p class="body-copy" style="position:relative;width:820px">Since the commencement of our activity, R. T. Holloway, Inc. contributes to change the quality of life of children and seniors across the world, providing them with support for primary education and basic medical aid, which we believe to be the right of every human being.</p>
  <a class="btn-outline" style="position:relative;margin-left:-55px">Read More</a>
</section>

<div class="footer-tab"></div>
<footer class="site-footer">
  <span class="footer-mark"></span>
  <div class="footer-name">R. T. Holloway</div>
  <div class="footer-sub">Inc.</div>
  <div class="contact-line">
    <span><svg viewBox="0 0 16 16"><path d="M8 0a5.5 5.5 0 0 0-5.5 5.5C2.5 10 8 16 8 16s5.5-6 5.5-10.5A5.5 5.5 0 0 0 8 0zm0 8a2.5 2.5 0 1 1 0-5 2.5 2.5 0 0 1 0 5z"/></svg>418 Alder Crest Avenue, New York, 10027.</span><span>|</span>
    <span><svg viewBox="0 0 16 16"><path d="M3.6 1l2.6 3-1.5 1.8c.9 2 2.5 3.6 4.5 4.5L11 8.8l3 2.6-1.4 2.9C7 14 2 9 1.7 3.4z"/></svg>555-210-4417.</span><span>|</span>
    <span><svg viewBox="0 0 16 16"><path d="M1 3h14v1.2L8 9 1 4.2zM1 6l7 4.8L15 6v7H1z"/></svg>info@rtholloway.com</span>
  </div>
  <nav class="footer-nav"><a>Home</a><a>About Us</a><a>Investment Areas</a><a>Social Responsibility</a><a>Contact Us</a></nav>
  <div class="social-links"><span></span><span></span><span></span><span></span></div>
  <div class="copyright">Copyright © 2021 All Rights Reserved.</div>
</footer>

</body>
</html>
```